Web re-design project www.vempresoft.com

We need a corporate website for a startup company called Vempre Labs. The company offers web-based worksite management system for big construction companies. In short, replacing annoying papers with iPads.
We need the site main page to provide basic overview of the company and then inner page layout for displaying news and detailed information about products.
Currently we have a site up at:
http://www.vempresoft.com/en/main
but as you can see the graphic design is a bit lacking in quality(implemented by a tech guy :)
We need you to pimp that web site design up!
There is possibility for more freelance work in the future related to our web products, slide show designs and printed marketing materials.
Our main product is LOMVI. You can find a short presentation about what it does here:
http://www.vempresoft.com/en/lomvi
Here you can find packages of images and screenshots related to our company:
https://files.plimbox.net/u/7719026/vempre_images.zip
https://files.plimbox.net/u/7719026/vempresoft%20images2.zip
Product logo svg can be found here:
https://files.plimbox.net/u/7719026/LOMVI-logo.svg
Your are not forced to use those images, but hopefully there will be something that is useful.
Hope to hear from you guys soon!
Cheers,
Ossi
Update:
We will be using LOMVI logo as the company brand. I don't like our current Vempre Labs company logo, so that doesn't need to be included in the site design.
Update 2:
I like website designs that are "light", elegant and pretty simplistic. One example is our product login page (screenshot included in files).
Update 3:
Sites from the same industry / type of products:
http://www.rakmoda.fi/
http://www.quarvelgrid.com/products/software/network-applications/fieldsync-3d
http://www.dornvex.com/construction/heavy-civil/software-solutions/Linked-Network.aspx?dtID=overview&
Target audience for the website is companies in the construction sector, and possibly corporate investors
Graphic Design

```html
<!DOCTYPE html>
<html lang="en">
<head>
<meta charset="utf-8">
<title>LOMVI – Worksite management</title>
<link href="https://fonts.googleapis.com/css2?family=PT+Sans:wght@400;700&family=PT+Sans+Narrow:wght@400;700&display=swap" rel="stylesheet">
<style>
:root{
  --red:#d9143a;
  --ink:#2b2b2b;
  --text:#555;
  --muted:#666;
  --band:#191919;
  --panel:#f2f2f2;
  --rule:#dcdcdc;
  --page:#ffffff;
}
*{margin:0;padding:0;box-sizing:border-box}
html,body{width:1200px;height:1131px;overflow:hidden;background:var(--page)}
body{font-family:"PT Sans Narrow",Arial,sans-serif;color:var(--text)}
.stage{position:absolute;left:0;top:0;width:1400px;height:1322px;transform:scale(.857143);transform-origin:0 0}
.site{position:absolute;left:200px;top:50px;width:1000px;height:1222px;background:#fff;box-shadow:0 0 8px rgba(0,0,0,.12)}
.abs{position:absolute}
a{text-decoration:none;color:inherit}

/* header */
.brand{left:17px;top:20px;display:flex;align-items:center;gap:12px}
.brand-dot{width:50px;height:50px;border-radius:50%;background:var(--ink)}
.brand-name{font-family:"PT Sans",Arial,sans-serif;font-size:40px;font-weight:400;color:var(--ink);letter-spacing:1px}
.main-nav{right:33px;top:34px;display:flex;gap:38px;font-size:19px;color:#333}
.main-nav .active{color:var(--red)}

/* hero */
.hero{left:0;top:89px;width:1000px;height:474px}
.hero-photo{position:absolute;inset:0 0 6px 0;background:linear-gradient(180deg,#0f64c2 0%,#3d8fd8 40%,#9cc3de 62%,#cdb27a 72%,#d8c7a3 100%)}
.hero-bar{position:absolute;left:0;bottom:0;width:100%;height:6px;background:var(--red)}
.hero-caption{position:absolute;left:0;top:374px;width:100%;height:94px;background:rgba(235,232,225,.72);padding:13px 19px}
.hero-caption h2{font-family:"PT Sans",Arial,sans-serif;font-size:18px;font-weight:700;color:var(--ink);margin-bottom:4px}
.hero-caption p{font-size:13.5px;line-height:22px;color:#333}

/* intro */
.intro-icon{left:57px;top:596px;width:40px;height:40px;border-radius:50%;background:var(--red)}
.section-title{font-size:19px;font-weight:700;color:#333;letter-spacing:.5px}
.intro-title{left:110px;top:604px}
.intro-text{left:56px;top:644px;width:570px;font-size:15px;line-height:24px;color:var(--text)}

/* news */
.news-title{left:673px;top:603px}
.news-thumb{left:673px;top:648px;width:82px;height:84px;border:1px solid #ddd;padding:3px;background:#fff}
.news-thumb div{width:100%;height:100%;background:linear-gradient(135deg,#f4f4f4,#c9ccd2 60%,#7e8796)}
.news-body{left:762px;top:647px;width:200px;font-size:13px;line-height:18px;color:var(--muted)}
.news-date{color:var(--red);font-family:"PT Sans",Arial,sans-serif;font-size:11px}
.news-more{color:var(--red);font-style:italic;font-family:"PT Sans",Arial,sans-serif;font-size:11px}

/* feature cards */
.card{top:781px;width:303px;height:342px;background:var(--panel)}
.card-photo{height:154px}
.card-band{position:relative;height:35px;background:var(--band);color:#fff;font-size:19px;letter-spacing:1px;padding:5px 0 0 37px}
.card-band:before{content:"";position:absolute;left:20px;top:-8px;border:8px solid transparent;border-top:0;border-bottom-color:var(--band)}
.card-text{padding:9px 22px 0 23px;font-size:13.5px;line-height:26px;color:var(--text)}
.card-rule{margin:8px 20px 0;border-top:1px solid #d6d6d6}
.card-link{display:block;padding:8px 0 0 38px;font-size:13.5px;color:var(--red)}
.photo-desk{background:linear-gradient(160deg,#d8d4cc,#8c8a86 60%,#4b4a50)}
.photo-plans{background:linear-gradient(160deg,#6c5a3a,#b79a6a 55%,#e2ddd2)}
.photo-frame{background:linear-gradient(180deg,#8fb4d8 0%,#c7a57a 55%,#b5553a 100%)}

/* footer */
.footer-rule{left:26px;top:1161px;width:948px;height:5px;background:var(--rule)}
.footer-nav{left:26px;top:1185px;display:flex;gap:21px;font-size:13.5px;color:#444}
.footer-nav .active{color:var(--red)}
.copyright{right:28px;top:1185px;font-size:13.5px;color:#444}
.copyright em{font-style:normal;color:var(--red)}
</style>
</head>
<body>
<div class="stage">
  <div class="site">
    <header>
      <a class="brand abs" href="#"><span class="brand-dot"></span><span class="brand-name">LOMVI</span></a>
      <nav class="main-nav abs">
        <a class="active" href="#">Home</a><a href="#">About</a><a href="#">Projects</a><a href="#">Services</a><a href="#">Blog</a><a href="#">Contact</a>
      </nav>
    </header>

    <section class="hero abs">
      <div class="hero-photo" role="img" aria-label="Site engineer in hard hat using a tablet beside an orange excavator under a blue sky"></div>
      <div class="hero-caption">
        <h2>Sungelle Molestie Elone</h2>
        <p>Lorem ipsum dolor sit amet, consectetur adipiscing elit. Praesent dolor nunc, rhoncus porttitor placerat sed dui raesent suscipit consequat nunc reedings eidolor nuncon forttitor eihonbin dum amet lorem pretium vulputate. Morbi purus dui, tempor sed imperdiet nec  vestibulum sed semper ac lorem pretium vulputate</p>
      </div>
      <div class="hero-bar"></div>
    </section>

    <section>
      <div class="intro-icon abs">
        <svg width="40" height="40" viewBox="0 0 40 40" aria-hidden="true">
          <g fill="#fff">
            <circle cx="20" cy="16" r="3.6"/><path d="M13.5 27c0-4.2 2.9-6.6 6.5-6.6s6.5 2.4 6.5 6.6z"/>
            <circle cx="13" cy="18" r="2.7"/><path d="M8 27c0-3.3 2.1-5.2 5-5.2 1 0 1.8.2 2.5.6-1.3 1.2-2 2.8-2 4.6z"/>
            <circle cx="27" cy="18" r="2.7"/><path d="M32 27c0-3.3-2.1-5.2-5-5.2-1 0-1.8.2-2.5.6 1.3 1.2 2 2.8 2 4.6z"/>
          </g>
        </svg>
      </div>
      <h3 class="section-title intro-title abs">LOREM IPSUM</h3>
      <p class="intro-text abs">Fusce egestas luctus lacus vitae hendrerit. Morbi vitae nibh erat aliquet diam. Curabitur odio mauris, suscipit non. Blandit iaculis, tempor quis velit. Sed consequat justo et massa bib eget malesuada sapien euismo am elementum tincidunt. Mauris tincidunt enim a tellus convallis in gravida eros adipiscing. Praesent at semper lectus. Nulla consequat tempor imperdiet.</p>
    </section>

    <aside>
      <h3 class="section-title news-title abs">LATEST NEWS</h3>
      <div class="news-thumb abs"><div role="img" aria-label="Presenter at a whiteboard in a meeting room"></div></div>
      <div class="news-body abs">
        <div class="news-date">12th October 2012</div>
        Praesent dolor nunc, rhoncus porttitorol bibendum in, placerat sed dui raesent suscipiten consequat nunc,<br><a class="news-more" href="#">more</a>
      </div>
    </aside>

    <article class="card abs" style="left:27px">
      <div class="card-photo photo-desk" role="img" aria-label="Hands drawing with a stylus on a tablet at a desk"></div>
      <div class="card-band">Headline One</div>
      <p class="card-text">Lorem ipsum dolor sit amet, consectetur adipis-ing elit. Praesent dolor nunc, rhoncus porttitorol bibendum in, placerat sed dui raesent suscipiten consequat nunc, etoni.</p>
      <div class="card-rule"></div>
      <a class="card-link" href="#">read more →</a>
    </article>
    <article class="card abs" style="left:350px">
      <div class="card-photo photo-plans" role="img" aria-label="Worker in hi-vis jacket reviewing plans on a tablet"></div>
      <div class="card-band">Headline One</div>
      <p class="card-text">Lorem ipsum dolor sit amet, consectetur adipis-ing elit. Praesent dolor nunc, rhoncus porttitorol bibendum in, placerat sed dui raesent suscipiten consequat nunc, etoni.</p>
      <div class="card-rule"></div>
      <a class="card-link" href="#">read more →</a>
    </article>
    <article class="card abs" style="left:673px">
      <div class="card-photo photo-frame" role="img" aria-label="Timber frame of a house under construction with stacked bricks"></div>
      <div class="card-band">Headline One</div>
      <p class="card-text">Lorem ipsum dolor sit amet, consectetur adipis-ing elit. Praesent dolor nunc, rhoncus porttitorol bibendum in, placerat sed dui raesent suscipiten consequat nunc, etoni.</p>
      <div class="card-rule"></div>
      <a class="card-link" href="#">read more →</a>
    </article>

    <footer>
      <div class="footer-rule abs"></div>
      <nav class="footer-nav abs"><a class="active" href="#">Home</a><a href="#">About</a><a href="#">Services</a><a href="#">Contact</a></nav>
      <div class="copyright abs">© 2012 <em>Vempre Labs</em> &nbsp;|&nbsp; All rights reserved</div>
    </footer>
  </div>
</div>
</body>
</html>
```